Drug safety monitoring company requires a new corporate website

We are an outsourcing partner to large and small companies within the pharmaceutical industry. Our current website www.quorvanta.co.uk has not been updated in a long time. We want a new web site that is responsive and modern but with a clearly corporate and professional feel. We want a design based on a 12 column grid system (mobile and desktop version). We want to use a new, modern font (not the standard web fonts) - we will purchase as required. Content can be used as is from the current website. Red and white are the corporate colours, so a palate should be developed to match. We do not need as much red as is in the current website. New icons (preferably in svg format) would be great. We can also purchase new images from Framly (or other) as required. We would prefer submissions in Sketch if possible.

Target Market(s)

Pharmaceutical companies

Number of Pages Required

1 page

Font styles to use
Sans Serif

Colors
ec1f27
ffffff

Requirements
Must have
• Design based on 12 column grid system.
Responsive design (i.e. require a mobile and desktop version).
How should the menu look between desktop and mobile?
A coherent colour palete.
Content to come from the existing website: www.quorvanta.co.uk
How should links be styled?
How should headings, sub-headings, paragraphs be styled?
Nice to have
• Custom developed icons (these are along the bottom of the page on the existing website: Medical Information; Pharmacovigilance; Literature Monitoring; Training).
New imagery (the images on the current website are dated).
Submission ideally as Sketch files (but we are okay with photoshop too).
A new, modern, non-standard font.
Not so much red in the design.
If we had buttons on the website, how should they be styled?
If we had a form on the website, how should the fields be styled?

```html
<!DOCTYPE html>
<html lang="en">
<head>
<meta charset="utf-8">
<title>Quorvanta Pharmacovigilance</title>
<link href="https://fonts.googleapis.com/css2?family=Montserrat:wght@400;500;600;700&family=Open+Sans:wght@400;600;700&display=swap" rel="stylesheet">
<style>
:root{
  --red:#ec1f27;
  --white:#ffffff;
  --ink:#1f2226;
  --body:#5d6167;
  --muted:#9a9ea4;
  --line:#e3e5e8;
  --soft:#f3f4f6;
  --dark:#1d1f22;
  --darker:#141517;
}
*{box-sizing:border-box;margin:0;padding:0}
html,body{width:1200px;height:5128px;overflow:hidden}
body{font-family:"Open Sans",Arial,sans-serif;color:var(--body);background:var(--white);font-size:13px;line-height:1.6}
h1,h2,h3,h4,.btn,.nav a,.brand{font-family:"Montserrat",Arial,sans-serif}
section,header,footer,.topbar{position:relative;width:1200px;overflow:hidden}
.ph{position:absolute;display:block}
.btn{display:inline-block;background:var(--red);color:var(--white);font-size:10px;font-weight:700;letter-spacing:.08em;text-transform:uppercase;padding:12px 26px;border-radius:2px;white-space:nowrap}
.btn.outline{background:var(--white);color:var(--ink);border:1px solid var(--ink);padding:11px 25px}
h2{font-size:30px;font-weight:700;color:var(--ink);line-height:1.2}
h3{font-size:15px;font-weight:600;color:var(--ink)}

/* top bar */
.topbar{height:32px;border-bottom:1px solid var(--line)}
.topbar .contact{position:absolute;left:640px;top:8px;font-size:10px;color:var(--muted)}
.topbar .contact span{margin-right:26px}
.topbar .dl{position:absolute;left:1030px;top:0;height:32px;width:170px;background:#d9dbde;color:#4c4f53;font-size:9px;font-weight:700;display:flex;align-items:center;justify-content:center;font-family:"Montserrat",sans-serif;letter-spacing:.05em}

/* header */
.site-header{height:112px}
.brand{position:absolute;left:228px;top:34px}
.brand .row{display:flex;align-items:center;gap:8px}
.brand .mark{width:14px;height:14px;background:var(--red);border-radius:50%}
.brand .name{font-size:22px;font-weight:700;color:var(--ink);letter-spacing:.06em;line-height:1}
.brand .sub{display:block;margin:6px 0 0 22px;font-size:8px;color:var(--muted);letter-spacing:.24em;font-weight:500}
.nav{position:absolute;left:470px;top:46px;display:flex;gap:30px}
.nav a{font-size:10px;font-weight:600;color:var(--ink);letter-spacing:.06em}
.nav a.active{color:var(--red);border-bottom:2px solid var(--red);padding-bottom:8px}
.nav a.login{color:var(--red)}

/* hero */
.hero{height:476px}
.hero .ph{inset:0;background:
  radial-gradient(ellipse 260px 300px at 900px 170px,#f4f7f9 0%,rgba(244,247,249,0) 70%),
  radial-gradient(ellipse 180px 140px at 980px 410px,#9fc2d6 0%,rgba(159,194,214,0) 75%),
  radial-gradient(ellipse 160px 120px at 720px 330px,#c98b6c 0%,rgba(201,139,108,0) 75%),
  linear-gradient(100deg,#58707e 0%,#7e96a3 28%,#b9cbd5 52%,#dde7ed 70%,#cfdde6 100%)}
.hero .copy{position:absolute;left:228px;top:130px;width:470px}
.hero h1{font-size:31px;line-height:1.3;font-weight:600;color:var(--white)}
.hero .btn{margin-top:30px}
.dots{position:absolute;left:576px;top:428px;display:flex;gap:8px}
.dots i{width:8px;height:8px;border-radius:50%;background:rgba(255,255,255,.55)}
.dots i:first-child{background:var(--white)}

/* services */
.services{height:580px}
.services .wrap{position:absolute;left:228px;top:100px;width:744px}
.services .intro{width:420px;margin-top:14px;font-size:11.5px}
.services .more{position:absolute;left:612px;top:48px}
.svc-grid{display:grid;grid-template-columns:repeat(3,1fr);gap:52px 40px;margin-top:48px}
.svc svg{width:34px;height:34px;stroke:var(--red);fill:none;stroke-width:2}
.svc h3{margin:10px 0 6px}
.svc p{font-size:11px;color:var(--muted);line-height:1.55}

/* welcome */
.welcome{height:600px}
.welcome .bg{position:absolute;left:-240px;top:0;width:520px;height:520px;border-radius:50%;background:var(--soft)}
.welcome .copy{position:absolute;left:40px;top:90px;width:540px}
.welcome .copy p{margin-top:12px;font-size:11.5px}
.welcome .copy b{color:var(--ink)}
.welcome .btn{margin-top:26px}
.welcome .pharmacist{left:700px;top:100px;width:500px;height:352px;background:
  radial-gradient(ellipse 90px 170px at 120px 190px,#ffffff 0%,rgba(255,255,255,0) 80%),
  radial-gradient(ellipse 60px 80px at 140px 60px,#d7b39a 0%,rgba(215,179,154,0) 80%),
  linear-gradient(90deg,#eef2f5 0%,#dfe6ec 30%,#b8c8d4 50%,#d9cfc4 70%,#9fb3c4 85%,#e7ecef 100%)}
.welcome .pills{left:600px;top:340px;width:260px;height:220px;background:
  radial-gradient(circle at 35% 55%,#ffffff 0%,rgba(255,255,255,0) 30%),
  radial-gradient(circle at 70% 40%,#e2423f 0%,rgba(226,66,63,0) 28%),
  radial-gradient(circle at 55% 75%,#f1c54a 0%,rgba(241,197,74,0) 25%),
  linear-gradient(135deg,#8fc6e3,#5aa3cc 55%,#3f84b0);box-shadow:0 8px 24px rgba(0,0,0,.18)}

/* about */
.about{height:528px}
.about .faint{left:0;top:0;width:480px;height:528px;background:
  radial-gradient(circle at 160px 160px,#e3e6ea 0%,rgba(227,230,234,0) 45%),
  radial-gradient(circle at 300px 360px,#e6e8eb 0%,rgba(230,232,235,0) 40%),
  linear-gradient(90deg,#f0f1f3,#f7f8f9 70%,#ffffff)}
.about .copy{position:absolute;left:500px;top:60px;width:472px}
.about .copy p{margin-top:14px;font-size:11.5px}
.about h3{margin-top:22px;font-size:17px;font-weight:700}
.icon-row{display:flex;gap:14px;margin-top:20px}
.icon-row span{width:40px;height:40px;border-radius:50%;border:2px solid var(--red);display:flex;align-items:center;justify-content:center}
.icon-row span.fill{background:var(--red)}
.about .btn{margin-top:30px}

/* stats */
.stats{height:244px;background:linear-gradient(90deg,var(--darker),#2d3034 50%,var(--darker))}
.stats .wrap{position:absolute;left:228px;top:56px;width:744px;display:grid;grid-template-columns:repeat(4,1fr);text-align:center;color:var(--white)}
.stats svg{width:28px;height:28px;stroke:var(--white);fill:none;stroke-width:2}
.stats .num{font-family:"Montserrat",sans-serif;font-size:36px;font-weight:700;line-height:1.3}
.stats .lbl{font-size:10px;color:#c7cacd;line-height:1.4}

/* team */
.team{height:396px}
.team h2{position:absolute;width:100%;text-align:center;top:74px}
.team .arrow{position:absolute;top:200px;font-size:30px;color:var(--ink);font-family:"Montserrat",sans-serif}
.member{position:absolute;top:140px;width:200px;text-align:center}
.member .ph{position:relative;width:190px;height:190px;border-radius:50%;margin:0 auto}
.m1 .ph{background:radial-gradient(ellipse 60px 90px at 50% 85%,#2d3f5c 0%,rgba(45,63,92,0) 90%),radial-gradient(circle at 50% 40%,#c9a68c 0%,rgba(201,166,140,0) 25%),linear-gradient(135deg,#aab6c2,#d7dde3 60%,#8997a6)}
.m2 .ph{background:radial-gradient(ellipse 60px 90px at 50% 85%,#222 0%,rgba(34,34,34,0) 90%),radial-gradient(circle at 50% 38%,#e0c08a 0%,rgba(224,192,138,0) 28%),linear-gradient(135deg,#eef0f2,#c8ced4 60%,#dfe3e7)}
.m3 .ph{background:radial-gradient(ellipse 60px 90px at 50% 85%,#1b1d22 0%,rgba(27,29,34,0) 90%),radial-gradient(circle at 50% 40%,#a97a5c 0%,rgba(169,122,92,0) 25%),linear-gradient(135deg,#c7c2b8,#e4e0da 55%,#8e8a84)}
.member h3{margin-top:14px;font-size:14px}
.member small{display:block;font-size:10px;color:var(--muted)}
.social{display:flex;gap:6px;justify-content:center;margin-top:8px}
.social i{width:18px;height:18px;border-radius:50%;background:var(--red)}

/* reviews */
.reviews{height:324px;background:var(--soft)}
.reviews .photo{right:0;top:0;width:560px;height:324px;background:
  radial-gradient(ellipse 140px 90px at 330px 130px,#f2b7b3 0%,rgba(242,183,179,0) 75%),
  radial-gradient(ellipse 90px 120px at 180px 220px,#e3c3ab 0%,rgba(227,195,171,0) 80%),
  linear-gradient(90deg,var(--soft),#dde4ea 25%,#bccbd8 60%,#d6dde4)}
.reviews .quote-mark{position:absolute;left:20px;top:10px;font-family:"Montserrat",sans-serif;font-size:280px;line-height:1;color:#e1e3e6;font-weight:700}
.reviews h2{position:absolute;left:228px;top:56px}
.review{position:absolute;left:228px;top:116px;width:440px;border-left:3px solid var(--red);padding-left:20px}
.stars{color:#f5a623;font-size:13px;letter-spacing:2px}
.review p{margin-top:6px;font-size:11px}
.review .who{display:flex;align-items:center;gap:10px;margin-top:14px}
.review .who i{width:34px;height:34px;border-radius:50%;background:#b9c1c9}
.review .who b{display:block;font-family:"Montserrat",sans-serif;font-size:12px;color:var(--ink);line-height:1.2}
.review .who small{font-size:10px;color:var(--muted)}

/* discover */
.discover{height:248px;text-align:center}
.discover h2{margin-top:76px;font-size:26px}
.discover p{font-size:11px;margin-top:6px}
.discover .btns{display:flex;gap:12px;justify-content:center;margin-top:18px}

/* blog */
.blog{height:560px}
.blog h2{text-align:center;margin-top:14px;font-size:28px}
.posts{position:absolute;left:228px;top:72px;width:744px;display:grid;grid-template-columns:repeat(3,1fr);gap:24px}
.post .ph{position:relative;height:168px}
.post:nth-child(1) .ph{background:radial-gradient(circle at 45% 40%,#e9d3c2 0%,rgba(233,211,194,0) 25%),radial-gradient(ellipse 70px 40px at 45% 55%,#9fd0e6 0%,rgba(159,208,230,0) 80%),linear-gradient(135deg,#c84a3e 0%,#d9a17c 30%,#7aa4c2 60%,#4f7c9e)}
.post:nth-child(2) .ph{background:radial-gradient(ellipse 50px 70px at 60% 45%,#ffffff 0%,rgba(255,255,255,0) 80%),linear-gradient(90deg,#e9ecef,#c9d3dc 40%,#e6b8a8 60%,#b4c4d2)}
.post:nth-child(3) .ph{background:radial-gradient(circle at 30% 40%,#fbe7a0 0%,rgba(251,231,160,0) 30%),linear-gradient(135deg,#f6d77c,#e9b54e 55%,#c9863a)}
.post h3{font-size:13px;font-weight:700;line-height:1.4;margin-top:14px}
.post a{display:block;color:var(--red);font-size:10px;font-weight:600;margin-top:8px}
.blog .btn{position:absolute;left:524px;top:498px}

/* message */
.message{height:672px}
.message .photo{left:0;top:0;width:300px;height:440px;background:
  radial-gradient(ellipse 70px 110px at 150px 170px,#8a5a2b 0%,rgba(138,90,43,0) 80%),
  radial-gradient(ellipse 120px 40px at 160px 360px,#f5f2ea 0%,rgba(245,242,234,0) 80%),
  linear-gradient(160deg,#f4f3ef,#e4ddd0 45%,#c9b89a 75%,#b49a74)}
.message .copy{position:absolute;left:592px;top:196px;width:380px}
.message h2{font-size:26px}
.message p{font-size:11px;margin-top:10px}
.form{margin-top:20px;display:flex;flex-direction:column;gap:8px}
.field{height:34px;background:#eceef0;font-size:10px;color:var(--muted);padding:10px 12px}
.field.area{height:92px}
.form .btn{align-self:flex-end;margin-top:14px}

/* footer */
.site-footer{height:356px;background:var(--dark);color:#b8bbbf}
.top-links{position:absolute;left:700px;top:84px;display:flex;gap:40px;font-size:10px;font-family:"Montserrat",sans-serif;font-weight:600;color:var(--white);letter-spacing:.06em}
.top-links span::before{content:"";display:inline-block;width:7px;height:7px;background:var(--red);border-radius:50%;margin-right:8px}
.f-brand{position:absolute;left:228px;top:70px}
.f-brand .name{font-family:"Montserrat",sans-serif;font-size:24px;font-weight:700;color:var(--white);letter-spacing:.08em;line-height:1.1}
.f-brand .sub{font-size:8px;letter-spacing:.24em;color:#9ca0a5;font-family:"Montserrat",sans-serif}
.f-col{position:absolute;top:150px;font-size:10px;line-height:1.8}
.f-col h4{font-size:11px;color:var(--white);font-weight:600;margin-bottom:6px}
.f-about{left:228px;width:170px}
.f-about .ph{position:relative;width:160px;height:72px;margin-top:10px;background:linear-gradient(180deg,#8fb0cf 0%,#c2d4e3 50%,#7d8c6a 70%,#4f6a43)}
.f-loc{left:440px;width:200px}
.f-map{left:700px;width:100px}
.f-sub{left:812px;width:160px}
.sub-field{display:flex;margin-top:6px}
.sub-field span{flex:1;height:26px;background:var(--white);font-size:9px;color:var(--muted);padding:5px 8px}
.sub-field b{width:26px;background:var(--red)}
.f-social{display:flex;gap:6px;margin-top:10px}
.f-social i{width:18px;height:18px;border-radius:50%;background:#4a4d52}
.copyright{position:absolute;left:0;right:0;bottom:0;height:44px;border-top:1px solid #33363a;font-size:9px;color:#84888d;padding:15px 228px}
</style>
</head>
<body>

<div class="topbar">
  <div class="contact"><span>+44 (0) 1632 960 418</span><span>hello@quorvanta.co.uk</span></div>
  <div class="dl">DOWNLOAD BROCHURE</div>
</div>

<header class="site-header">
  <div class="brand"><div class="row"><span class="mark"></span><span class="name">QUORVANTA</span></div><span class="sub">PHARMACOVIGILANCE</span></div>
  <nav class="nav">
    <a class="active">HOME</a><a>ABOUT US</a><a>QPPV</a><a>OUR SERVICES</a><a>CONTACT US</a><a class="login">● CLIENT LOGIN</a>
  </nav>
</header>

<section class="hero">
  <div class="ph" role="img" aria-label="Laboratory scientist in mask and gloves pipetting samples into test tubes"></div>
  <div class="copy">
    <h1>At Quorvanta We Ensure That Your Business Has The Best Pharmacovigilance Support In The Industry</h1>
    <span class="btn">Request Free Consultation</span>
  </div>
  <div class="dots"><i></i><i></i><i></i></div>
</section>

<section class="services">
  <div class="wrap">
    <h2>Our Services</h2>
    <p class="intro">We provide a range of professional services to the pharmaceutical industry, in order to ensure your products meet every safety requirement.</p>
    <span class="btn more">Learn More</span>
    <div class="svc-grid">
      <div class="svc">
        <svg viewBox="0 0 34 34"><rect x="6" y="4" width="22" height="26" rx="2"/><path d="M11 12h12M11 18h12M11 24h7"/></svg>
        <h3>Eudravigilance</h3><p>Registration with the Eudravigilance Pharmacovigilance Portal and licence holder support.</p>
      </div>
      <div class="svc">
        <svg viewBox="0 0 34 34"><rect x="4" y="10" width="26" height="14" rx="7"/><path d="M17 10v14"/></svg>
        <h3>Pharmacovigilance</h3><p>Ensure regulatory standards are fully met, compliant with current pharmacovigilance guidance.</p>
      </div>
      <div class="svc">
        <svg viewBox="0 0 34 34"><path d="M17 6v22M6 17h22"/><circle cx="17" cy="17" r="13"/></svg>
        <h3>Medical Information</h3><p>Professional enquiry handling to support the safe and effective use of your products.</p>
      </div>
      <div class="svc">
        <svg viewBox="0 0 34 34"><path d="M4 8h11v20H4zM19 8h11v20H19z"/></svg>
        <h3>Literature Monitoring</h3><p>Product safety through surveillance of published articles and case reports.</p>
      </div>
      <div class="svc">
        <svg viewBox="0 0 34 34"><rect x="6" y="12" width="22" height="16" rx="2"/><path d="M12 12V7h10v5M17 16v8M13 20h8"/></svg>
        <h3>Medical Devices</h3><p>Medical devices are governed by the relevant regulation and vigilance requirements.</p>
      </div>
      <div class="svc">
        <svg viewBox="0 0 34 34"><path d="M3 13l14-7 14 7-14 7z"/><path d="M9 16v7c4 4 12 4 16 0v-7"/></svg>
        <h3>Training</h3><p>Complete training support for pharmacovigilance teams and staff.</p>
      </div>
    </div>
  </div>
</section>

<section class="welcome">
  <div class="bg"></div>
  <div class="copy">
    <h2>Welcome</h2>
    <p>Welcome to the <b>Quorvanta Pharmacovigilance</b> website. We are an <b>outsourcing partner</b> to large and small companies within the <b>pharmaceutical industry</b>. Our range of services is tailored to suit each of our clients, whether for human or veterinary medicinal products.</p>
    <p><b>Pharmacovigilance</b> is defined by WHO as "the science and activities relating to the detection, assessment, understanding and prevention of adverse effects or any other drug-related problem". The service is one of <b>managing risk</b> associated with medicinal products so as to protect patients.</p>
    <p>Our <b>primary functions</b> are QPPV and related <b>pharmacovigilance services</b> to assist and support Marketing Authorisation Holders with pharmacovigilance systems, in line with the requirements of the regulatory authorities.</p>
    <p>The regulatory environment is ever changing and we aim to keep our clients up to date with all developments that affect them, working as a <b>close partner</b> at all times.</p>
    <span class="btn">Download Our Company Brochure</span>
  </div>
  <div class="ph pharmacist" role="img" aria-label="Pharmacist in white coat holding a tablet between pharmacy shelves"></div>
  <div class="ph pills" role="img" aria-label="Assorted tablets and capsules on a blue surface"></div>
</section>

<section class="about">
  <div class="ph faint" role="img" aria-label="Faint molecular structure backdrop"></div>
  <div class="copy">
    <h2>About Us</h2>
    <p>Quorvanta Pharmacovigilance operates from offices in Marlow and provides services to clients across Europe. We are an outsourcing provider of medical information enquiry handling, pharmacovigilance and QPPV services, working with companies of all sizes in the pharmaceutical sector.</p>
    <h3>Our Services</h3>
    <p>We provide a range of services to support the pharmaceutical industry, with a focus on handling product safety data, literature searching and regulatory compliance.</p>
    <div class="icon-row">
      <span class="fill"><svg width="18" height="18" viewBox="0 0 18 18" fill="none" stroke="#fff" stroke-width="2"><path d="M9 2v14M2 9h14"/></svg></span>
      <span><svg width="18" height="18" viewBox="0 0 18 18" fill="none" stroke="#ec1f27" stroke-width="2"><circle cx="9" cy="8" r="5"/><path d="M9 13v3"/></svg></span>
    </div>
    <span class="btn">Learn More</span>
  </div>
</section>

<section class="stats">
  <div class="wrap">
    <div><svg viewBox="0 0 28 28"><circle cx="14" cy="10" r="5"/><path d="M4 25c2-6 18-6 20 0"/></svg><div class="num">99%</div><div class="lbl">Client Satisfaction<br>Guaranteed</div></div>
    <div><svg viewBox="0 0 28 28"><rect x="4" y="6" width="20" height="18" rx="2"/><path d="M4 11h20"/></svg><div class="num">98%</div><div class="lbl">Turnaround Time<br>Met Each Year</div></div>
    <div><svg viewBox="0 0 28 28"><path d="M5 15l6 6 12-14"/></svg><div class="num">96%</div><div class="lbl">Quality Assured<br>Projects</div></div>
    <div><svg viewBox="0 0 28 28"><circle cx="14" cy="14" r="10"/><path d="M14 8v6l4 3"/></svg><div class="num">98%</div><div class="lbl">Clients Rate Us<br>Independent Accuracy</div></div>
  </div>
</section>

<section class="team">
  <h2>Our Team</h2>
  <span class="arrow" style="left:228px">‹</span>
  <span class="arrow" style="left:960px">›</span>
  <div class="member m1" style="left:266px"><span class="ph" role="img" aria-label="Portrait of a team member in a dark suit"></span><h3>Name Surname</h3><small>Company Position</small><div class="social"><i></i><i></i><i></i></div></div>
  <div class="member m2" style="left:500px"><span class="ph" role="img" aria-label="Portrait of a team member in a bright office"></span><h3>Name Surname</h3><small>Company Position</small><div class="social"><i></i><i></i><i></i></div></div>
  <div class="member m3" style="left:734px"><span class="ph" role="img" aria-label="Portrait of a team member at a desk"></span><h3>Name Surname</h3><small>Company Position</small><div class="social"><i></i><i></i><i></i></div></div>
</section>

<section class="reviews">
  <div class="ph photo" role="img" aria-label="Hand holding a blister pack of pink tablets"></div>
  <div class="quote-mark">“</div>
  <h2>Client Reviews</h2>
  <div class="review">
    <div class="stars">★★★★★</div>
    <p>Lorem ipsum dolor sit amet, consectetur adipiscing elit, sed do eiusmod tempor incididunt ut labore et dolore magna aliqua. Ut enim ad minim veniam, quis nostrud exercitation ullamco laboris nisi ut aliquip ex ea commodo consequat.</p>
    <div class="who"><i></i><div><b>Name Surname</b><small>Company Position</small></div></div>
  </div>
</section>

<section class="discover">
  <h2>Discover How We Can Help</h2>
  <p>Free consultation and assessment of your business requirements</p>
  <div class="btns"><span class="btn">Contact Us</span><span class="btn outline">Download Our Brochure</span></div>
</section>

<section class="blog">
  <h2>Explore Our Latest Blog Posts</h2>
  <div class="posts">
    <div class="post"><span class="ph" role="img" aria-label="Doctor wearing a face mask in a clinic"></span><h3>Lorem ipsum dolor sit amet, consectetur adipiscing elit, sed do eiusmod tempor</h3><a>Read More ›</a></div>
    <div class="post"><span class="ph" role="img" aria-label="Pharmacist checking shelves of medicine"></span><h3>Lorem ipsum dolor sit amet, consectetur adipiscing elit, sed do eiusmod tempor</h3><a>Read More ›</a></div>
    <div class="post"><span class="ph" role="img" aria-label="Pile of yellow tablets"></span><h3>Lorem ipsum dolor sit amet, consectetur adipiscing elit, sed do eiusmod tempor</h3><a>Read More ›</a></div>
  </div>
  <span class="btn">Read More Articles</span>
</section>

<section class="message">
  <div class="ph photo" role="img" aria-label="Brown medicine bottle with spilled white capsules on a table"></div>
  <div class="copy">
    <h2>Send Us A Message</h2>
    <p>Lorem ipsum dolor sit amet, consectetur adipiscing elit, sed do eiusmod tempor incididunt ut labore et dolore magna aliqua, ut enim ad minim veniam.</p>
    <div class="form">
      <div class="field">Your Name</div>
      <div class="field">Your Email</div>
      <div class="field">Your Contact Number</div>
      <div class="field area">Your Message</div>
      <span class="btn">Send</span>
    </div>
  </div>
</section>

<footer class="site-footer">
  <div class="f-brand"><div class="name">QUORVANTA</div><div class="sub">PHARMACOVIGILANCE</div></div>
  <div class="top-links"><span>CLIENT LOGIN</span><span>DOWNLOAD OUR BROCHURE</span></div>
  <div class="f-col f-about">
    Lorem ipsum dolor sit amet, we ensure your business has the best pharmacovigilance support in the industry.
    <span class="ph" role="img" aria-label="Office building exterior under a blue sky"></span>
  </div>
  <div class="f-col f-loc">
    <h4>Business Location</h4>
    Meridian House, Hollin Lane<br>Marlow, Buckinghamshire<br>SL7 4QX<br>
    ☎ +44 (0) 1632 960 418<br>✉ hello@quorvanta.co.uk
    <div class="f-social"><i></i><i></i><i></i><i></i></div>
  </div>
  <div class="f-col f-map">
    <h4>Site Map</h4>Home<br>About Us<br>QPPV<br>Our Services<br>Contact Us
  </div>
  <div class="f-col f-sub">
    <h4>Subscribe To Our Newsletter</h4>
    <div class="sub-field"><span>Your Email</span><b></b></div>
  </div>
  <div class="copyright">Copyright © 2024 Quorvanta Ltd. All rights reserved.</div>
</footer>

</body>
</html>
```